Label & logo reformatting & improving

7 labels I had designed and paid for by a Halvery graphic designer working at Halvery Morning Ledger. Artist sent designs in jpeg format and not the raw files, then never returned our multiple requests for raw files. Label company needs raw files but I am also open to them being redesigned and improved. Or perhaps just background imaging i.e. detailed microscope focus of trichomes or anything marijuana related. Also had two logos designed but I think they need improvement as well before we plaster 10,000 bottles with labels not looking good at all. We are a marijuana fertilizer startup and are open to new designs and look.

```html
<!DOCTYPE html>
<html lang="en">
<head>
<meta charset="utf-8">
<title>Gilded Root Hydroponics – Grow Big Label</title>
<link rel="stylesheet" href="https://fonts.googleapis.com/css2?family=Montserrat:ital,wght@0,400;0,500;1,800&family=Open+Sans:wght@600&display=swap">
<style>
  :root {
    --artboard: #d1d2d4;
    --label: #ffffff;
    --gold: #d9b86c;
    --lavender: #cfcce8;
    --sage: #97a86c;
    --ink-grey: #58595b;
  }
  * { margin: 0; padding: 0; box-sizing: border-box; }
  html, body {
    width: 1200px;
    height: 1000px;
    overflow: hidden;
    background: var(--artboard);
  }
  .label {
    position: absolute;
    left: 331px;
    top: 125px;
    width: 538px;
    height: 750px;
    background: var(--label);
    text-align: center;
  }
  .brand-mark {
    position: absolute;
    top: 76px;
    left: 0;
    width: 100%;
    display: flex;
    justify-content: center;
    align-items: center;
    gap: 8px;
    font-family: "Montserrat", sans-serif;
    font-weight: 500;
    font-size: 30px;
    letter-spacing: 2px;
    color: var(--gold);
  }
  .brand-mark .dot {
    width: 14px;
    height: 14px;
    border-radius: 50%;
    background: var(--gold);
  }
  .brand-name {
    position: absolute;
    top: 144px;
    left: 0;
    width: 100%;
    font-family: "Montserrat", sans-serif;
    font-weight: 500;
    font-size: 20px;
    line-height: 23px;
    letter-spacing: 1.2px;
    color: var(--gold);
  }
  .emblem {
    position: absolute;
    left: 107px;
    top: 218px;
    width: 324px;
    height: 324px;
  }
  .headline {
    position: absolute;
    top: 563px;
    left: 0;
    width: 100%;
    font-family: "Montserrat", sans-serif;
    font-style: italic;
    font-weight: 800;
    font-size: 48px;
    line-height: 49px;
    letter-spacing: -1.5px;
    color: var(--gold);
    text-transform: uppercase;
  }
  .net-contents {
    position: absolute;
    top: 683px;
    left: 0;
    width: 100%;
    font-family: "Open Sans", sans-serif;
    font-weight: 600;
    font-size: 15.5px;
    line-height: 20px;
    color: var(--ink-grey);
  }
</style>
</head>
<body>
  <main class="label">
    <div class="brand-mark"><span class="dot"></span><span>GRH</span></div>
    <p class="brand-name">Gilded Root<br>Hydroponics</p>

    <svg class="emblem" viewBox="0 0 324 324" xmlns="http://www.w3.org/2000/svg">
      <defs>
        <radialGradient id="mascot-fill" cx="50%" cy="52%" r="50%">
          <stop offset="0%" stop-color="var(--sage)"/>
          <stop offset="45%" stop-color="#b3b89f"/>
          <stop offset="100%" stop-color="var(--lavender)"/>
        </radialGradient>
      </defs>
      <circle cx="162" cy="162" r="153" fill="url(#mascot-fill)" role="img" aria-label="Mascot illustration: a muscular green cannabis bud character flexing its arms, surrounded by leaves"/>
      <circle cx="162" cy="162" r="153.5" fill="none" stroke="var(--gold)" stroke-width="17"/>
    </svg>

    <h1 class="headline">Grow Big<br>or Go Home</h1>

    <p class="net-contents">16oz (0.473 liters)<br>Net Weight - 1 lb (0.454 kg)</p>
  </main>
</body>
</html>
```